Magical healing ointment looking for new branded labels

I need a new product label for my healing comfrey ointments, which started as just a simple ointment, and has grown to include a few varients including a body oil and lip balm. It sells quite well when I have a market, which I don't always have time to do - so I'd like to take it and leave it with some health shops, however for this I'd really like a more professional label to take these products further.

The company name is Brightmere Quill - slogan Pure from Roots; as I am both a healer that makes ointments and yet also make scarves, cowls with high quality natural wool.
The ointment is simply called 'Comfrey Ointment', don't mind if it has Magical or healing in front of it. It's made by me, with high quality all natural, locally sourced organic ingredients, and supports the healing of bones, injuries, RSI, arthritis, rheuma, eczema, aches and pains.. Comfrey itself is an ancient herb also used in medieval herblore and by the ancient romans, so my keys words are to get feeling for the brand:
Timeless/ classic/ clean/ natural/ quality/ confident/ healing

I would like the labels to stand out, and look professional. The smallest size is 6 x 2.5 cm, this is an amber small jar of 30ml, the larger jar is double that size at 60ml, and the bottles bigger. I would like to be able to add a bit on the side if needed to add ingredients, and be able to scale the label up or down depending on the size of the jar. On top of this would like to be able to text as needed depending on the product in the jar.

Have included my company logo - for an idea of what that looks like, please note though that this branding or style doesn't need to include this logo, nor look like this logo. I've also included an example of someone who I think is doing a good job of being unique, simple, classic and appealing. Let me know if you have any questions. Thanks!

Target Market(s)

People with an eco-sustainable mind-set that are looking to resolve ailments naturally.

Industry/Entity Type

Health

Requirements
Must have
• The product name, and company name
Nice to have
• I'd like to leave most of the design to the designers ideas, however am ok to have leaves - or natural elements that support the typography, but not overwhelm it.

```html
<!DOCTYPE html>
<html lang="en">
<head>
<meta charset="utf-8">
<title>Brightmere Quill – Healing Comfrey Label</title>
<link rel="stylesheet" href="https://fonts.googleapis.com/css2?family=Arimo:wght@700&family=Bodoni+Moda:wght@400&family=Quicksand:wght@300&family=Roboto+Condensed:wght@300&display=swap">
<style>
  :root {
    --page: #ffffff;
    --label: #ffffff;
    --frame: #3a3a3a;
    --ink: #1c1c1c;
    --copy: #555555;
    --sun: #fdbd0e;
    --botanical: #f4dfd0;
    --botanical-soft: #fbf1ea;
  }
  * { box-sizing: border-box; margin: 0; padding: 0; }
  html, body {
    width: 1200px;
    height: 1000px;
    overflow: hidden;
    background: var(--page);
  }
  .canvas {
    position: relative;
    width: 1200px;
    height: 1000px;
  }
  .label {
    position: absolute;
    left: 73px;
    top: 47px;
    width: 1059px;
    height: 442px;
    background: var(--label);
    border: 1px solid var(--frame);
    overflow: hidden;
  }
  .label__botanical {
    position: absolute;
    inset: 0 0 41px 0;
    background:
      radial-gradient(ellipse 260px 200px at 720px 110px, var(--botanical) 0%, transparent 70%),
      radial-gradient(ellipse 220px 260px at 980px 200px, var(--botanical) 0%, transparent 70%),
      radial-gradient(ellipse 240px 220px at 120px 330px, var(--botanical) 0%, transparent 70%),
      radial-gradient(ellipse 200px 180px at 420px 80px, var(--botanical) 0%, transparent 70%),
      var(--botanical-soft);
    opacity: 0.75;
  }
  .label__band {
    position: absolute;
    left: 0;
    right: 0;
    bottom: 0;
    height: 41px;
    background: var(--sun);
  }
  .label__claims {
    position: absolute;
    left: 18px;
    top: 124px;
    width: 270px;
  }
  .label__headline {
    font-family: "Arimo", Arial, sans-serif;
    font-weight: 700;
    font-size: 17px;
    line-height: 23px;
    color: var(--copy);
  }
  .label__benefits {
    margin-top: 14px;
    font-family: "Roboto Condensed", "Arial Narrow", sans-serif;
    font-weight: 300;
    font-size: 17px;
    line-height: 23.5px;
    color: var(--copy);
    text-transform: uppercase;
  }
  .brand {
    position: absolute;
    left: 316px;
    top: 120px;
    width: 424px;
    text-align: center;
  }
  .brand__slogan {
    font-family: "Quicksand", Arial, sans-serif;
    font-weight: 300;
    font-size: 15px;
    letter-spacing: 4px;
    text-transform: uppercase;
    color: var(--sun);
  }
  .brand__rule {
    height: 0;
    border-top: 2px solid var(--ink);
    margin: 8px 0;
  }
  .brand__name {
    font-family: "Bodoni Moda", Georgia, serif;
    font-weight: 400;
    font-size: 44px;
    line-height: 48px;
    color: var(--ink);
  }
  .brand__mark {
    position: absolute;
    left: 50%;
    top: 50%;
    width: 18px;
    height: 18px;
    margin-left: -9px;
    border-radius: 50%;
    background: var(--sun);
  }
  .product-name {
    position: absolute;
    left: 316px;
    top: 298px;
    width: 424px;
    text-align: center;
    font-family: "Quicksand", Arial, sans-serif;
    font-weight: 300;
    font-size: 32px;
    color: var(--ink);
  }
</style>
</head>
<body>
  <main class="canvas">
    <section class="label">
      <div class="label__botanical" role="img" aria-label="Faint engraved botanical illustration of comfrey leaves, stems and bell flowers in pale peach"></div>
      <div class="label__band"></div>

      <div class="label__claims">
        <p class="label__headline">All natural, locally sourced organic ingredients</p>
        <p class="label__benefits">Supports the healing of bones, injuries, RSI, arthritis, rheuma, eczema, aches and pains</p>
      </div>

      <div class="brand">
        <p class="brand__slogan">Pure from Roots</p>
        <div class="brand__rule"></div>
        <h1 class="brand__name">Brightmere Quill</h1>
        <div class="brand__rule"></div>
      </div>

      <p class="product-name">Healing Comfrey</p>
    </section>
  </main>
</body>
</html>
```